Bright Tail Botanicals: Extracts for Pets

We need a brochure to help market the products. Bright Tail Botanicals makes Chinese Herbal Extracts for cats and dogs. We have three products to launch with. An allergy, calming, and pain formula. They are based on traditional Chinese Medicine Formulas that have been used for hundreds of years on humans and animals. I would like the logo (attached) and have one or two cat/dogs pictures. They can be any of the pics from my website. Each product should have a descrition of what it treats (can pull from website). The brochure can highlight its convient, effective, and a safe alternative. It has to include:

This statement has not been evaluated by the FDA.
This product is not intended to diagnose, treat, cure,
or prevent any disease. Bright Tail is not liable for any adverse effects.

I included a sample with some of the important info for the products - the desing does not have to be similar, just an example of the copy

*I would like the format to be in Illustrator, vector, so that I can change sizes if I need to without loosing any detail.

Target Market(s)

Pet Owners

Industry/Entity Type

Pet Care

Font styles to use
Other font styles liked:
• Universal (as logo)

Requirements
Must have
• Logo, Description of each products.
Nice to have
• Dog or cat picture

```html
<!DOCTYPE html>
<html lang="en">
<head>
<meta charset="utf-8">
<title>Bright Tail Botanicals – Extracts for Pets</title>
<link rel="stylesheet" href="https://fonts.googleapis.com/css2?family=Lato:wght@400;700;900&family=Oswald:wght@400;500;700&display=swap">
<style>
  :root {
    --page: #e4e4e4;
    --lime: #a6d93a;
    --green: #7dbb2f;
    --navy: #1f3f7a;
    --blue: #2e5fa8;
    --ink: #2b2b2b;
    --logo-green: #5e8a34;
    --bottle: #5b2a1c;
    --photo-warm: #c9a84a;
  }
  html, body {
    margin: 0;
    width: 1200px;
    height: 1200px;
    overflow: hidden;
    background: var(--page);
  }
  .brochure {
    position: absolute;
    left: 0;
    top: 138px;
    width: 1200px;
    height: 923px;
    display: block;
  }
  .heading { font-family: "Oswald", sans-serif; font-weight: 500; fill: #fff; }
  .benefits { font-family: "Lato", sans-serif; font-size: 23px; fill: var(--ink); }
  .panel-copy { font-family: "Lato", sans-serif; font-size: 19.5px; fill: #fff; }
  .cta-small { font-family: "Lato", sans-serif; font-weight: 700; font-size: 31px; fill: var(--ink); }
  .cta-big { font-family: "Oswald", sans-serif; font-weight: 700; font-size: 58px; fill: #1d1d1d; }
  .brand-name { font-family: "Lato", sans-serif; font-weight: 700; font-size: 30px; fill: var(--logo-green); }
  .web { font-family: "Lato", sans-serif; font-size: 29px; fill: var(--ink); }
</style>
</head>
<body>
<svg class="brochure" viewBox="0 0 1222 940" preserveAspectRatio="none" xmlns="http://www.w3.org/2000/svg">
  <defs>
    <linearGradient id="bg-right" x1="0" y1="0" x2="1" y2="1">
      <stop offset="0" stop-color="#fafafa"/>
      <stop offset="0.6" stop-color="#dedede"/>
      <stop offset="1" stop-color="#c8c8c8"/>
    </linearGradient>
    <linearGradient id="photo-tones" x1="0" y1="0" x2="0" y2="1">
      <stop offset="0" stop-color="#b7a85a"/>
      <stop offset="0.35" stop-color="#8fae45"/>
      <stop offset="1" stop-color="var(--photo-warm)"/>
    </linearGradient>
    <linearGradient id="bar-green" x1="0" x2="1">
      <stop offset="0" stop-color="#2f6b35"/>
      <stop offset="1" stop-color="#4f8f3c"/>
    </linearGradient>
    <linearGradient id="bar-blue" x1="0" x2="1">
      <stop offset="0" stop-color="#1d4f94"/>
      <stop offset="1" stop-color="#3a72c0"/>
    </linearGradient>
    <linearGradient id="bar-crimson" x1="0" x2="1">
      <stop offset="0" stop-color="#9c1a3e"/>
      <stop offset="1" stop-color="#c7365c"/>
    </linearGradient>
    <linearGradient id="panel-blue" x1="0" y1="0" x2="1" y2="1">
      <stop offset="0" stop-color="var(--navy)"/>
      <stop offset="0.6" stop-color="var(--blue)"/>
      <stop offset="1" stop-color="var(--navy)"/>
    </linearGradient>
    <radialGradient id="cta-fill" cx="0.5" cy="0.4" r="0.6">
      <stop offset="0" stop-color="#b9e34c"/>
      <stop offset="1" stop-color="#6fae2a"/>
    </radialGradient>
    <linearGradient id="lime-band" x1="0" x2="1">
      <stop offset="0" stop-color="var(--lime)"/>
      <stop offset="1" stop-color="var(--green)"/>
    </linearGradient>
  </defs>

  <!-- right background -->
  <rect class="backdrop" width="1222" height="940" fill="url(#bg-right)" role="img" aria-label="Faded grey photo of a dog resting in tall grass"/>

  <!-- lime sweep and bottom strip -->
  <path class="lime-sweep" d="M600,470 C720,530 850,620 874,790 C884,850 900,812 950,812 L1222,812 L1222,940 L0,940 L0,560 Z" fill="url(#lime-band)"/>

  <!-- blue copy panel -->
  <path class="copy-panel" d="M0,605 L560,548 C680,560 820,640 850,800 C870,870 860,905 820,915 L0,915 Z" fill="url(#panel-blue)"/>

  <!-- photo frame: green edge, white edge, photo -->
  <path class="photo-edge-green" d="M0,0 H470 C492,120 600,230 615,390 L625,520 L0,605 Z" fill="var(--green)"/>
  <path class="photo-edge-white" d="M0,0 H447 C468,120 582,230 598,385 L607,505 L0,578 Z" fill="#fff"/>
  <path class="photo" d="M0,0 H432 C452,120 566,230 583,385 L590,495 L0,560 Z" fill="url(#photo-tones)" role="img" aria-label="Photo of two brindle puppies sitting in autumn grass"/>

  <!-- call to action -->
  <circle cx="555" cy="488" r="104" fill="#fff"/>
  <circle cx="555" cy="488" r="92" fill="url(#cta-fill)"/>
  <text class="cta-small" x="555" y="476" text-anchor="middle">CALL US</text>
  <text class="cta-big" x="555" y="530" text-anchor="middle">TODAY</text>

  <!-- brand block -->
  <rect class="brand-block" x="55" y="563" width="234" height="377" fill="#fff"/>
  <circle cx="172" cy="690" r="58" fill="var(--logo-green)" opacity="0.85"/>
  <text class="brand-name" x="172" y="812" text-anchor="middle">BRIGHT TAIL</text>
  <text class="brand-name" x="172" y="850" text-anchor="middle">BOTANICALS</text>

  <!-- panel copy -->
  <text class="panel-copy" text-anchor="end">
    <tspan x="775" y="676">Formulated by Licensed Herbalist trained in</tspan>
    <tspan x="775" y="700">Traditional Chinese Medicine. Extracts based on</tspan>
    <tspan x="775" y="724">formulas that have safely treated animals and</tspan>
    <tspan x="775" y="748">humans for over hundreds of years.</tspan>
    <tspan x="775" y="772">Testimonials at brighttailbotanicals.com</tspan>
    <tspan x="775" y="821">This statement has not been evaluated by the FDA.</tspan>
    <tspan x="775" y="845">This product is not intended to diagnose, treat, cure,</tspan>
    <tspan x="775" y="869">or prevent any disease. Bright Tail is not liable</tspan>
  </text>

  <text class="web" x="875" y="870">www.brighttail.co.uk</text>

  <!-- product: allergies -->
  <path class="bar" d="M675,115 H950 A22,22 0 0 1 950,158 H675 Z" fill="url(#bar-green)"/>
  <text class="heading" x="711" y="148" font-size="29" textLength="172" lengthAdjust="spacingAndGlyphs">ALLERGIES &amp; ITCH</text>
  <text class="benefits"><tspan x="711" y="193">Itching, Sinusitis, Red Eyes, Dermatitis,</tspan><tspan x="711" y="222">Eczema, Rash, Mucus</tspan></text>
  <rect x="600" y="60" width="78" height="178" rx="8" fill="var(--bottle)" role="img" aria-label="Allergy and itch extract dropper bottle"/>
  <rect x="626" y="23" width="26" height="40" rx="4" fill="#1e1e1e"/>

  <!-- product: pain -->
  <path class="bar" d="M745,346 H1163 A21,21 0 0 1 1163,388 H745 Z" fill="url(#bar-blue)"/>
  <text class="heading" x="767" y="378" font-size="28" textLength="389" lengthAdjust="spacingAndGlyphs">PAIN: ANTI-INFLAMMATORY &amp; ANALGESIC</text>
  <text class="benefits"><tspan x="777" y="426">Arthritis,Hip Dysplasia,ACL,Muscle</tspan><tspan x="777" y="455">and Joint Pain,Spinal Injury</tspan></text>
  <rect x="672" y="296" width="78" height="184" rx="8" fill="var(--bottle)" role="img" aria-label="Pain relief extract dropper bottle"/>
  <rect x="698" y="258" width="26" height="40" rx="4" fill="#1e1e1e"/>

  <!-- product: calming -->
  <path class="bar" d="M905,571 H1038 A22,22 0 0 1 1038,615 H905 Z" fill="url(#bar-crimson)"/>
  <text class="heading" x="931" y="604" font-size="29" textLength="89" lengthAdjust="spacingAndGlyphs">CALMING</text>
  <text class="benefits"><tspan x="931" y="648">Anxiety, Hyperactivity,</tspan><tspan x="931" y="677">Trauma, Seizures, Hy-</tspan><tspan x="931" y="706">pertension, OCD</tspan></text>
  <rect x="832" y="524" width="76" height="176" rx="8" fill="var(--bottle)" role="img" aria-label="Calming extract dropper bottle"/>
  <rect x="857" y="486" width="26" height="40" rx="4" fill="#1e1e1e"/>
</svg>
</body>
</html>
```